Solace Chiropractic & Acupuncture Business Cards

I need a business card design that feels elevated. I am open to any of the logo designs uploaded. We have two doctors so I'll need to be able to change out the names.

Information:
Marnie Toller D.C., L.Ac., CCSP
584 W 12th St, Ste 320
Fairmont, NE 67419
solacegrove.net
402-555-0147
drmarnie@solacegrove.com
Updates

We have designs we like now, we are just trying to choose between top contenders. Thanks for your submissions!

Contact Information for Business Card

noted in description

Requirements
Must have
• ability to edit info if possible
Nice to have
• Please see our website solacegrove.net for our style and colors

```html
<!DOCTYPE html>
<html lang="en">
<head>
<meta charset="utf-8">
<title>Solace Chiropractic &amp; Acupuncture – Business Card</title>
<link rel="stylesheet" href="https://fonts.googleapis.com/css2?family=Playfair+Display:wght@400;500&display=swap">
<style>
  :root {
    --page: #f2f2f2;
    --paper: #f0f1eb;
    --navy: #343d50;
    --sand: #d2c9bf;
    --white: #ffffff;
  }
  * { margin: 0; padding: 0; box-sizing: border-box; }
  html, body { width: 1200px; height: 1200px; overflow: hidden; background: var(--page); }
  .canvas { position: relative; width: 1200px; height: 1200px; font-family: "Playfair Display", Georgia, serif; color: var(--navy); }
  .card { position: absolute; left: 238px; width: 723px; height: 402px; background: var(--paper); overflow: hidden; }
  .card--front { top: 184px; }
  .card--back { top: 614px; }

  .front-mark { position: absolute; left: 0; top: 0; width: 100%; height: 100%; display: flex; flex-direction: column; align-items: center; justify-content: center; gap: 18px; }
  .front-mark__dot { width: 72px; height: 72px; border-radius: 50%; background: var(--sand); }
  .front-mark__name { font-size: 17px; font-weight: 400; letter-spacing: 3px; text-transform: uppercase; color: var(--navy); text-align: center; }

  .back-band { position: absolute; left: 0; top: 0; width: 723px; height: 402px; }
  .doctor { position: absolute; left: 60px; top: 50px; color: var(--paper); font-weight: 400; letter-spacing: 1.5px; white-space: nowrap; }
  .doctor__name { font-size: 27px; }
  .doctor__credentials { font-size: 17px; margin-left: 4px; }

  .practice-name { position: absolute; left: 55px; top: 186px; font-size: 19px; font-weight: 400; color: var(--navy); line-height: 1.25; }

  .contact { position: absolute; display: flex; align-items: flex-start; gap: 15px; font-size: 18.5px; line-height: 24px; white-space: nowrap; }
  .contact__icon { flex: none; width: 31px; height: 31px; border-radius: 50%; background: var(--navy); display: flex; align-items: center; justify-content: center; margin-top: -4px; }
  .contact__icon svg { width: 17px; height: 17px; }
  .contact--address { left: 47px; top: 270px; }
  .contact--web { left: 47px; top: 343px; }
  .contact--phone { left: 366px; top: 270px; }
  .contact--email { left: 366px; top: 343px; }
</style>
</head>
<body>
<div class="canvas">

  <section class="card card--front">
    <div class="front-mark">
      <div class="front-mark__dot"></div>
      <p class="front-mark__name">Solace Chiropractic &amp; Acupuncture</p>
    </div>
  </section>

  <section class="card card--back">
    <svg class="back-band" viewBox="0 0 723 402" aria-hidden="true">
      <path d="M0 0 H723 V136 C640 170 520 178 400 160 C300 146 230 112 140 116 C80 118 30 132 0 152 Z" fill="var(--navy)"/>
      <path d="M30 136 C110 112 210 118 320 146 C430 176 520 190 665 163 C560 196 440 196 330 168 C220 140 130 126 30 136 Z" fill="var(--sand)"/>
    </svg>

    <h1 class="doctor"><span class="doctor__name">MARNIE TOLLER</span><span class="doctor__credentials">D.C., L.AC., CCSP</span></h1>

    <p class="practice-name">Solace Chiropractic &amp;<br>Acupuncture</p>

    <div class="contact contact--address">
      <span class="contact__icon"><svg viewBox="0 0 24 24" fill="none" stroke="var(--white)" stroke-width="1.6"><path d="M12 22s-7-7.5-7-12.5a7 7 0 0 1 14 0C19 14.5 12 22 12 22z"/><circle cx="12" cy="9.5" r="2.5"/></svg></span>
      <span>584 W 12th St, Ste 320<br>Fairmont, NE 67419</span>
    </div>

    <div class="contact contact--web">
      <span class="contact__icon"><svg viewBox="0 0 24 24" fill="none" stroke="var(--white)" stroke-width="1.5"><circle cx="12" cy="12" r="9"/><ellipse cx="12" cy="12" rx="4" ry="9"/><path d="M3 12h18M4.5 7.5h15M4.5 16.5h15"/></svg></span>
      <span>solacegrove.net</span>
    </div>

    <div class="contact contact--phone">
      <span class="contact__icon"><svg viewBox="0 0 24 24" fill="var(--white)"><path d="M6.6 3.5l2.6-.6 1.7 4.2-2 1.5a11 11 0 0 0 6.5 6.5l1.5-2 4.2 1.7-.6 2.6c-.3 1.2-1.4 2-2.6 1.9C10.9 18.8 5.2 13.1 4.7 6.1c-.1-1.2.7-2.3 1.9-2.6z"/></svg></span>
      <span>402-555-0147</span>
    </div>

    <div class="contact contact--email">
      <span class="contact__icon"><svg viewBox="0 0 24 24" fill="none" stroke="var(--white)" stroke-width="1.6"><rect x="3" y="6" width="18" height="12"/><path d="M3 6l9 7 9-7M3 18l7-6M21 18l-7-6"/></svg></span>
      <span>drmarnie@solacegrove.com</span>
    </div>
  </section>

</div>
</body>
</html>
```